Zielgruppe
Steuerberatung
Aufgabenstellung
Ich benötige eine Neuerstellung für ein vorhandenes Briefpapier. Bedeutet, eigentlich soll der aktuelle Inhalt neu erstellt werden, da mir die Rohdaten nicht mehr zur Verfügung stehen. Das aktuelle Briefpapier steht als .doc zur Verfügung. Ziel 1:1 Abbildung. Zudem muss die Adresse geändert werden.

```html
<!DOCTYPE html>
<html lang="de">
<head>
<meta charset="utf-8">
<title>Briefpapier – Konrad Wellmer Steuerberater</title>
<link rel="stylesheet" href="https://fonts.googleapis.com/css2?family=Archivo+Narrow:wght@400;700&display=swap">
<style>
  :root {
    --ink: #111111;
    --paper: #ffffff;
    --watermark: #e4e4e4;
  }
  * { margin: 0; padding: 0; box-sizing: border-box; }
  html, body { width: 847px; height: 1200px; overflow: hidden; background: var(--paper); }
  body { font-family: "Archivo Narrow", "Arial Narrow", sans-serif; color: var(--ink); }
  .sheet { position: relative; width: 847px; height: 1200px; overflow: hidden; background: var(--paper); }

  .sender-line {
    position: absolute; left: 79px; top: 178px;
    font-size: 8px; white-space: nowrap;
  }

  .brand {
    position: absolute; left: 615px; top: 66px;
    display: flex; align-items: center; gap: 6px;
    font-size: 12px; font-weight: 700; white-space: nowrap;
  }
  .brand-square { width: 10px; height: 10px; background: var(--ink); }

  .contact {
    position: absolute; left: 615px; top: 177px;
    font-size: 11.5px; line-height: 17.3px; white-space: nowrap;
  }
  .contact dl { display: grid; grid-template-columns: 31px auto; }
  .name { font-weight: 700; }
  .sep { margin: 0 4px; }

  .watermark-name {
    position: absolute; right: -40px; bottom: -40px;
    font-size: 260px; font-weight: 700; line-height: 1;
    color: var(--watermark); white-space: nowrap;
  }

  .footer {
    position: absolute; left: 79px; top: 1110px;
    font-size: 11px; line-height: 17px; white-space: nowrap;
  }
  .bottom-rule {
    position: absolute; left: 0; right: 0; bottom: 1px; height: 1px; background: var(--ink);
  }
</style>
</head>
<body>
<main class="sheet">
  <div class="watermark-name" aria-hidden="true">Wellmer</div>

  <div class="brand"><span class="brand-square"></span>Konrad Wellmer</div>

  <p class="sender-line">Konrad Wellmer<span class="sep">|</span>Lindenauer Str. 27<span class="sep">|</span>31234 Nordheim</p>

  <section class="contact">
    <p><span class="name">Konrad Wellmer</span><span class="sep">|</span>Steuerberater</p>
    <dl>
      <dt>Tel.:</dt><dd>+49 (0) 170 - 55 01 236</dd>
      <dt>Fax.:</dt><dd>+49 (0) 500 - 12 34 56 78</dd>
      <dt>Mail:</dt><dd>info@steuerberatung-wellmer.de</dd>
      <dt>Web:</dt><dd>www.steuerberatung-wellmer.de</dd>
    </dl>
  </section>

  <footer class="footer">
    <p><span class="name">Konrad Wellmer</span><span class="sep">|</span>Steuerberater</p>
    <p>Lindenauer Str. 27<span class="sep">|</span>31234 Nordheim<span class="sep">|</span>Zuständige Aufsichtsbehörde: Steuerberaterkammer Nordland -Körperschaft des öffentlichen Rechts-</p>
    <p>Zuständiges Finanzamt: Finanzamt Nordheim-Mitte, Steuernummer: 31/208/40917<span class="sep">|</span>Bankverbindung: DE 00 1234 5678 9012 3456 78 BIC: NOBKDE2X</p>
  </footer>

  <div class="bottom-rule"></div>
</main>
</body>
</html>
```